Webbanner-Design für Affiliate Marketing
Zielgruppe
Online-Shop für Kopfbedeckungen aller Art (Hüte, Mützen, Fascinator, Stirnbänder)
Design soll eine möglichst große Zielgruppe ansprechen (Hauptfokus: 18-34 Jahre). Also alle Online-Shopper mit einer Vorliebe für Hüte/ Mützen.
Aufgabenstellung
Insgesamt ein modernes, eingängiges und stilvolles Design. Nicht allzu verspielt oder zu unruhig. Fokus auf das Wesentliche.
Text: A Headwear for Everyone
B Hüte und Mützen, Top Auswahl, Kostenlose Lieferung
C Gut behütet durch den Winter
D Der Hut-Online-Shop
Das Lumo Vanta Logo soll mit eingebunden werden. Keine vorgegebene Platzierung, sprich dem Design anpassen.
Formate: (Breite x Höhe)
1. Full Banner - 468 x 60 Pixel, max. 40k Dateigröße
2. Medium Rectangle - 300 x 250 Pixel, max. 40k Dateigröße
3. Vertical Banner - 120 x 240 Pixel, max. 30k Dateigröße
4. Rectangle - 180 x 150 Pixel, max. 40k Dateigröße

```html
<!DOCTYPE html>
<html lang="de">
<head>
<meta charset="utf-8">
<title>Lumo Vanta – Webbanner</title>
<link href="https://fonts.googleapis.com/css2?family=Poppins:wght@400;600;700&display=swap" rel="stylesheet">
<style>
  :root {
    --canvas: #ffffff;
    --cta: #ff4b4b;
    --text-light: #ffffff;
    --brand-dark: #1e1e1e;
    --rule: rgba(255,255,255,0.85);
  }
  * { margin: 0; padding: 0; box-sizing: border-box; }
  html, body {
    width: 1200px; height: 1051px; overflow: hidden;
    background: var(--canvas);
    font-family: "Poppins", sans-serif;
  }
  .canvas { position: relative; width: 1200px; height: 1051px; }
  .banner {
    position: absolute; width: 480px; height: 400px; overflow: hidden;
    color: var(--text-light);
  }
  .banner--headwear { left: 96px; top: 96px; }
  .banner--winter { left: 624px; top: 96px; }
  .banner--selection { left: 96px; top: 544px; }
  .banner--shop { left: 624px; top: 544px; }

  .banner__photo { position: absolute; inset: 0; }
  .banner--headwear .banner__photo {
    background: linear-gradient(100deg, #3a2a22 0%, #5b3a3a 35%, #7a5560 55%, #b8a593 80%, #d8cbbb 100%);
  }
  .banner--winter .banner__photo {
    background: linear-gradient(90deg, #3d3835 0%, #6f6560 40%, #b8a9a0 65%, #c65b2b 78%, #8a8583 100%);
  }
  .banner--selection .banner__photo {
    background: linear-gradient(110deg, #3a2c22 0%, #6b4a33 40%, #8f5d3c 60%, #4a3a30 85%, #2c2824 100%);
  }
  .banner--shop .banner__photo {
    background: linear-gradient(95deg, #2a2a2a 0%, #3b3f48 35%, #5d6068 55%, #6d6548 75%, #4e4a3c 100%);
  }

  .brand-tag {
    position: absolute; background: #fff; display: flex; align-items: center;
    justify-content: center; gap: 8px; color: var(--brand-dark);
    font-weight: 600; font-size: 15px; letter-spacing: 0.5px; text-transform: uppercase;
  }
  .brand-tag__dot { width: 18px; height: 18px; border-radius: 50%; background: var(--brand-dark); }
  .banner--headwear .brand-tag, .banner--shop .brand-tag { left: 0; top: 0; height: 61px; padding: 0 14px; }
  .banner--selection .brand-tag { right: 0; top: 0; width: 88px; height: 91px; }
  .banner--selection .brand-tag__dot { width: 56px; height: 56px; }

  .headline {
    position: absolute; font-weight: 700; text-transform: uppercase;
    line-height: 1; text-shadow: 0 2px 8px rgba(0,0,0,0.25);
  }
  .banner--headwear .headline {
    left: 0; right: 0; top: 176px; text-align: center; font-size: 52px; line-height: 59px;
    letter-spacing: -0.5px;
  }
  .banner--winter .headline { left: 16px; top: 92px; font-size: 66px; line-height: 77px; }
  .banner--selection .headline { left: 16px; top: 46px; font-size: 66px; line-height: 72px; }
  .banner--shop .headline { left: 16px; top: 80px; font-size: 66px; line-height: 69px; }

  .subline {
    position: absolute; left: 16px; font-weight: 600; text-transform: uppercase;
    text-shadow: 0 1px 6px rgba(0,0,0,0.3);
  }
  .banner--winter .subline { top: 246px; font-size: 28px; }
  .banner--selection .subline { top: 276px; font-size: 20px; letter-spacing: 0.2px; }

  .rule { position: absolute; left: 16px; height: 2px; background: var(--rule); }
  .banner--headwear .rule { top: 296px; width: 448px; }
  .banner--winter .rule { top: 285px; width: 320px; }
  .banner--selection .rule { top: 261px; width: 440px; }
  .banner--shop .rule { top: 291px; width: 184px; }

  .cta {
    position: absolute; left: 16px; width: 272px; height: 64px; background: var(--cta);
    display: flex; align-items: center; justify-content: center;
    font-size: 27px; font-weight: 400; color: var(--text-light);
  }
  .banner--headwear .cta, .banner--winter .cta, .banner--selection .cta { top: 320px; }
  .banner--shop .cta { top: 314px; }
</style>
</head>
<body>
<main class="canvas">

  <section class="banner banner--headwear">
    <div class="banner__photo" role="img" aria-label="Frau mit dunkelviolettem Filzhut vor einer alten Holzfassade"></div>
    <div class="brand-tag"><span class="brand-tag__dot"></span>Lumo Vanta</div>
    <h2 class="headline">A Headwear<br>for Everyone</h2>
    <div class="rule"></div>
    <a class="cta">Jetzt kaufen</a>
  </section>

  <section class="banner banner--winter">
    <div class="banner__photo" role="img" aria-label="Frau mit orangefarbener Strickmütze und hellem Haar"></div>
    <h2 class="headline">Gut<br>behütet</h2>
    <p class="subline">Durch den Winter</p>
    <div class="rule"></div>
    <a class="cta">Jetzt kaufen</a>
  </section>

  <section class="banner banner--selection">
    <div class="banner__photo" role="img" aria-label="Frau mit rotem Haar und schwarzem Hut im Profil"></div>
    <div class="brand-tag" aria-label="Lumo Vanta"><span class="brand-tag__dot"></span></div>
    <h2 class="headline">Hüte<br>und<br>Mützen</h2>
    <div class="rule"></div>
    <p class="subline">Top Auswahl · Kostenlose Lieferung</p>
    <a class="cta">Jetzt kaufen</a>
  </section>

  <section class="banner banner--shop">
    <div class="banner__photo" role="img" aria-label="Hand hält einen olivgrünen Filzhut mit braunem Lederband"></div>
    <div class="brand-tag"><span class="brand-tag__dot"></span>Lumo Vanta</div>
    <h2 class="headline">Der Hut<br>Online<br>Shop</h2>
    <div class="rule"></div>
    <a class="cta">Jetzt kaufen</a>
  </section>

</main>
</body>
</html>
```